Business Card Design Project

Need a business card which is crisp, clear and modern.
with the logo being highlighted and at the back of the card our services.
Please use the attached logo for creating the cards.

Reason: need to receive some good designs

Our target customers will be hotels, offices, single users

Business

```html
<!DOCTYPE html>
<html lang="en">
<head>
<meta charset="utf-8">
<title>Tellwave Business Card</title>
<link rel="stylesheet" href="https://fonts.googleapis.com/css2?family=Didact+Gothic&family=Montserrat:wght@700&display=swap">
<style>
  :root {
    --stage: #d6d6d4;
    --card-white: #f4f4f4;
    --card-black: #141414;
    --ink: #1a1a1a;
    --ink-soft: #333333;
    --paper-white: #ffffff;
    --accent: #e8336b;
  }
  * { box-sizing: border-box; margin: 0; padding: 0; }
  html, body {
    width: 1200px;
    height: 900px;
    overflow: hidden;
    background: var(--stage);
  }
  .stage {
    position: relative;
    width: 1200px;
    height: 900px;
  }
  .card {
    position: absolute;
    left: 320px;
    width: 560px;
    height: 320px;
    overflow: hidden;
    border-radius: 4px;
    box-shadow: 0 6px 18px rgba(0,0,0,0.18);
  }
  .card--back {
    top: 80px;
    background: linear-gradient(180deg, #1e1e1e 0%, var(--card-black) 100%);
    display: flex;
    align-items: center;
    justify-content: center;
  }
  .card--front {
    top: 460px;
    background: linear-gradient(135deg, var(--paper-white) 0%, var(--card-white) 100%);
  }
  .brand {
    display: flex;
    align-items: center;
    gap: 14px;
    font-family: "Montserrat", sans-serif;
    font-weight: 700;
    letter-spacing: 1px;
  }
  .brand__dot {
    border-radius: 50%;
    background: var(--accent);
    flex: none;
  }
  .card--back .brand { color: var(--paper-white); font-size: 52px; }
  .card--back .brand__dot { width: 60px; height: 60px; }
  .card--front .brand {
    position: absolute;
    left: 30px;
    top: 26px;
    color: var(--ink);
    font-size: 34px;
  }
  .card--front .brand__dot { width: 44px; height: 44px; }
  .person {
    position: absolute;
    left: 40px;
    top: 96px;
  }
  .person__name {
    font-family: "Montserrat", sans-serif;
    font-weight: 700;
    font-size: 30px;
    color: var(--ink);
    line-height: 1.1;
  }
  .person__title {
    font-family: "Didact Gothic", sans-serif;
    font-size: 16px;
    color: var(--ink-soft);
  }
  .contacts {
    position: absolute;
    left: 22px;
    top: 170px;
    list-style: none;
    font-family: "Didact Gothic", sans-serif;
    font-size: 16px;
    color: var(--ink);
  }
  .contacts__item {
    display: flex;
    align-items: center;
    height: 26px;
  }
  .contacts__icon { width: 18px; height: 18px; margin-right: 6px; }
  .contacts__label {
    font-family: "Montserrat", sans-serif;
    font-weight: 700;
    font-size: 14px;
    width: 62px;
  }
  .bands {
    position: absolute;
    left: 0;
    top: 0;
    width: 560px;
    height: 320px;
  }
</style>
</head>
<body>
<main class="stage">
  <section class="card card--back" aria-label="Card back">
    <div class="brand"><span class="brand__dot"></span>Tellwave</div>
  </section>

  <section class="card card--front" aria-label="Card front">
    <svg class="bands" viewBox="0 0 560 320" aria-hidden="true">
      <polygon points="0,262 330,262 362,300 0,300" fill="var(--card-black)"/>
      <polygon points="420,290 560,290 560,320 440,320" fill="var(--card-black)"/>
    </svg>

    <div class="brand"><span class="brand__dot"></span>Tellwave</div>

    <div class="person">
      <p class="person__name">Name</p>
      <p class="person__title">titele</p>
    </div>

    <ul class="contacts">
      <li class="contacts__item">
        <svg class="contacts__icon" viewBox="0 0 20 20" aria-hidden="true">
          <circle cx="10" cy="10" r="8.5" fill="none" stroke="var(--ink)" stroke-width="1.5"/>
          <path d="M7 5.5l2 2-1 1.3c.6 1.4 1.7 2.5 3.2 3.2l1.3-1 2 2-1.2 1.5c-3.5-.4-6.4-3.3-6.8-6.8z" fill="var(--ink)"/>
        </svg>
        <span class="contacts__label">Tel:</span>
        <span>(555) 014-2290</span>
      </li>
      <li class="contacts__item">
        <svg class="contacts__icon" viewBox="0 0 20 20" aria-hidden="true">
          <rect x="2" y="5" width="16" height="11" fill="var(--ink)"/>
          <path d="M2 5l8 6 8-6" fill="none" stroke="var(--paper-white)" stroke-width="1.3"/>
        </svg>
        <span class="contacts__label">Email:</span>
        <span>hello@tellwave.example</span>
      </li>
      <li class="contacts__item">
        <svg class="contacts__icon" viewBox="0 0 20 20" aria-hidden="true">
          <g fill="none" stroke="var(--ink)" stroke-width="1.3">
            <circle cx="10" cy="10" r="8"/>
            <ellipse cx="10" cy="10" rx="3.5" ry="8"/>
            <path d="M2 10h16M3.5 6h13M3.5 14h13"/>
          </g>
        </svg>
        <span class="contacts__label">Web:</span>
        <span>www.tellwave.example</span>
      </li>
    </ul>
  </section>
</main>
</body>
</html>
```